Independent Financial Advisor Billboard Campaign - Granite Bridge Financial

I am a local, independent financial advisor. My company is Granite Bridge Financial, located in Charleston, WV. My main source of revenue comes from those nearing or entering retirement that need assistance with financial planning and investment management. Many are looking to rollover their employer retirement plan into an IRA account. I would like a billboard design campaign that focuses on this type of client. Please see our website www.granitebridgefinancial-example.com for more information.

```html
<!DOCTYPE html>
<html lang="en">
<head>
<meta charset="UTF-8">
<title>Granite Bridge Financial – Retirement Done Right Billboard</title>
<link href="https://fonts.googleapis.com/css2?family=Montserrat:ital,wght@0,700;0,800;1,800;1,900&display=swap" rel="stylesheet">
<style>
  :root {
    --page-bg: #eceef1;
    --board-white: #fbfbfb;
    --brand-blue: #0d55a0;
    --band-blue: #16427f;
    --ink: #141416;
    --photo-light: #e4e6ea;
    --photo-mid: #c9ced6;
    --portrait-top: #d9cfc4;
    --portrait-bottom: #f1f2f4;
  }
  * { margin: 0; padding: 0; box-sizing: border-box; }
  html, body {
    width: 1200px;
    height: 1200px;
    overflow: hidden;
    background: var(--page-bg);
  }
  .billboard {
    position: absolute;
    left: 20px;
    top: 350px;
    width: 1160px;
    height: 500px;
    background: var(--board-white);
    overflow: hidden;
    box-shadow: 0 10px 30px rgba(0,0,0,0.15);
  }
  .backdrop-photo {
    position: absolute;
    inset: 0 0 170px 0;
    background: linear-gradient(120deg, var(--board-white) 15%, var(--photo-light) 45%, var(--photo-mid) 60%, var(--photo-light) 75%, var(--board-white) 95%);
    opacity: 0.7;
  }
  .phone-band {
    position: absolute;
    left: 0;
    right: 0;
    bottom: 0;
    height: 170px;
    background: var(--band-blue);
  }
  .advisor-portrait {
    position: absolute;
    left: 20px;
    bottom: 0;
    width: 250px;
    height: 400px;
    background: linear-gradient(180deg, var(--portrait-top) 0%, var(--portrait-top) 40%, var(--portrait-bottom) 48%, var(--portrait-bottom) 100%);
    border-radius: 110px 110px 0 0;
  }
  .headline {
    position: absolute;
    left: 290px;
    top: 30px;
    width: 850px;
    font-family: 'Montserrat', sans-serif;
    font-style: italic;
    font-weight: 900;
    font-size: 112px;
    line-height: 1;
    letter-spacing: 2px;
    color: var(--brand-blue);
    text-align: center;
    white-space: nowrap;
  }
  .tagline {
    position: absolute;
    left: 425px;
    top: 178px;
    width: 420px;
    padding: 14px 0 12px;
    border-top: 3px solid var(--ink);
    border-bottom: 3px solid var(--ink);
    font-family: 'Montserrat', sans-serif;
    font-weight: 800;
    font-size: 54px;
    line-height: 1;
    letter-spacing: 1px;
    color: var(--ink);
    text-align: center;
    white-space: nowrap;
  }
  .phone-number {
    position: absolute;
    left: 290px;
    bottom: 0;
    width: 870px;
    height: 170px;
    display: flex;
    align-items: center;
    justify-content: center;
    font-family: 'Montserrat', sans-serif;
    font-style: italic;
    font-weight: 800;
    font-size: 94px;
    line-height: 1;
    letter-spacing: 1px;
    color: #ffffff;
    white-space: nowrap;
  }
</style>
</head>
<body>
  <main class="billboard">
    <div class="backdrop-photo" role="img" aria-label="Faded photo of modern office towers seen from below"></div>
    <div class="phone-band"></div>
    <div class="advisor-portrait" role="img" aria-label="Portrait photo of the financial advisor in a white polo shirt"></div>
    <h1 class="headline">RETIREMENT</h1>
    <p class="tagline">DONE RIGHT</p>
    <p class="phone-number">304-555-0142</p>
  </main>
</body>
</html>
```